Agribusiness Insurance

I would like postcard designed to attract farmers and agribusiness owners to my insurance consulting services. My business model is being a Trusted Advisor through identifying exposures, developing strategies, implementing programs and then monitoring our designed plan. I am knowledge representative (13YRs ag insurance), Represent 15 Farm + Carriers (favorable pricing/competitive multiple options) Specialized in Confinements, Cattle Farms, and Grain Producers. No Membership Fees Necessary

Many Insurance Producers in my area are nearing retirement I am 33 and am looking to promote this..

Target Market(s)

Farmers and Agribusiness Owners

Industry/Entity Type

Agribusiness

Requirements
Must have

• Toby Halvern
Phone: Cell 555 207 4816
Email: thalvern@ruralplexadvice.example

```html
<!DOCTYPE html>
<html lang="en">
<head>
<meta charset="utf-8">
<title>Agribusiness Insurance Postcard</title>
<link rel="stylesheet" href="https://fonts.googleapis.com/css2?family=Open+Sans:wght@400;700&family=Roboto+Condensed:wght@700&display=swap">
<style>
  :root {
    --paper: #ffffff;
    --ink: #111111;
    --sky: #dfe6ea;
    --crop-green: #4f8a35;
    --wheat: #b89a63;
    --barn-steel: #5d6168;
    --feed-green: #7aa64a;
  }
  * { margin: 0; padding: 0; box-sizing: border-box; }
  html, body { width: 1200px; height: 930px; overflow: hidden; background: var(--paper); }
  .postcard { position: relative; width: 1200px; height: 930px; background: var(--paper); color: var(--ink); }

  .photo { position: absolute; left: 30px; width: 376px; }
  .photo--crop-duster { top: 30px; height: 283px;
    background: linear-gradient(to bottom, var(--sky) 0%, #d6dde2 55%, #e9eeee 62%, var(--crop-green) 72%, #3f7428 100%); }
  .photo--combine { top: 319px; height: 287px;
    background: linear-gradient(to bottom, #eef1f3 0%, #c9d1d6 25%, #4c5a63 40%, #6b6a5c 52%, var(--wheat) 58%, #a88752 100%); }
  .photo--dairy-barn { top: 612px; height: 288px;
    background: linear-gradient(to bottom, var(--barn-steel) 0%, #7d838a 30%, #3a3d40 55%, var(--feed-green) 80%, #e9ece6 100%); }

  .pitch {
    position: absolute; left: 445px; top: 98px;
    font-family: "Open Sans", sans-serif; font-size: 20px; line-height: 28.6px;
  }
  .contact {
    position: absolute; left: 445px; top: 561px;
    font-family: "Roboto Condensed", sans-serif; font-weight: 700; font-size: 20px; line-height: 28.6px;
  }
  .indicia {
    position: absolute; left: 938px; top: 37px; width: 219px; height: 218px;
    border: 3px solid var(--ink); border-radius: 3px;
    display: flex; align-items: center; justify-content: center;
    font-family: "Open Sans", sans-serif; font-size: 25px; line-height: 29.5px;
    text-align: center; text-transform: uppercase;
  }
  .indicia strong { font-weight: 700; }
</style>
</head>
<body>
<main class="postcard">
  <div class="photo photo--crop-duster" role="img" aria-label="Crop-dusting plane spraying a green field"></div>
  <div class="photo photo--combine" role="img" aria-label="Combine harvester in a golden wheat field"></div>
  <div class="photo photo--dairy-barn" role="img" aria-label="Dairy cows feeding in an open-sided barn"></div>

  <p class="pitch">
    My business model is being a<br>
    Trusted Advisor through<br>
    identifying exposures,<br>
    developing strategies,<br>
    implementing programs and<br>
    then monitoring our designed<br>
    plan. I am knowledge<br>
    representative (13years<br>
    experience in agricultural<br>
    insurance), represent 15 Farm +<br>
    Carriers (favorable<br>
    pricing/competitive multiple<br>
    options) Specialized in<br>
    Confinements, Cattle Farms,<br>
    and Grain Producers.
  </p>

  <p class="contact">
    TOBY HALVERN<br>
    Phone: Cell 555 207 4816<br>
    Email: thalvern@ruralplexadvice.example
  </p>

  <div class="indicia">
    <p>Presorted<br>Standard<br>US Postage<br><strong>Paid</strong><br>Canton, OH<br>Permit #2418</p>
  </div>
</main>
</body>
</html>
```